Landingpage design for Movarabroker website

We need a design for a responsive 1 page landing page.
Good example: https://www.kelvaro.com/
On the homepage we will like to have a explanation video
attached you can find the logo's

About the website Movara.offers:
Movara.offers is a “Broker” we bring buyers and sellers together and facilitate transactions

Simple
quickly
Actuel
Compare (who is the best provider, at what price)
great offer
independent
1 invoice

Target Market(s)

BtoB

Number of Pages Required

1 page

Requirements
Must have
• On the homepage we will like to have a explanation video
Nice to have
• something between shipper and carrier and bring them togheter
• We will focus us first on fish transport... maybe you can add something
• Map from europe that shows our workarea

```html
<!DOCTYPE html>
<html lang="en">
<head>
<meta charset="utf-8">
<title>Movara Offers – Landing page</title>
<link href="https://fonts.googleapis.com/css2?family=Open+Sans:wght@400;600;700&display=swap" rel="stylesheet">
<style>
:root{
  --ink:#2b2f36;
  --navy:#252a34;
  --blue:#29a8df;
  --sky:#aee6f7;
  --paper:#f6f6f6;
  --white:#ffffff;
  --muted:#d9dde2;
  --kraft:#8a7256;
}
*{box-sizing:border-box;margin:0;padding:0}
html,body{width:1200px;height:3047px;overflow:hidden}
body{font-family:"Open Sans",Arial,sans-serif;color:var(--ink);background:var(--white);position:relative}
section,header,footer{position:absolute;left:0;width:1200px}
.abs{position:absolute}
p{font-size:11px;line-height:21px}

/* brand */
.brand{display:flex;align-items:center;gap:10px;font-weight:700;font-size:20px;color:var(--blue);letter-spacing:.5px;text-transform:uppercase}
.brand-dot{width:28px;height:28px;border-radius:50%;background:var(--blue)}

/* hero */
.hero{top:0;height:561px;background:var(--white);overflow:hidden}
.hero-shape{position:absolute;inset:0}
.site-nav{position:absolute;top:12px;left:234px;width:732px;height:30px}
.site-nav .brand{position:absolute;left:0;top:0}
.nav-login{position:absolute;left:535px;top:8px;font-size:9px;font-weight:600;color:var(--ink)}
.nav-register{position:absolute;left:577px;top:0;width:86px;height:29px;background:var(--navy);color:var(--white);font-size:9px;font-weight:600;display:flex;align-items:center;justify-content:center}
.nav-icons{position:absolute;left:690px;top:4px}
.hero-title{left:258px;top:198px;font-size:22px;line-height:32px;font-weight:700;color:var(--ink)}
.hero-copy{left:258px;top:290px;width:200px}
.hero-copy p{margin-bottom:14px;line-height:15px;font-size:10.5px}
.video{left:616px;top:240px;width:350px;height:197px;background:linear-gradient(135deg,#6b4a3a,#2c1e18);}
.video-bar{position:absolute;left:0;bottom:0;width:100%;height:22px;background:rgba(20,20,20,.85)}
.video-play{position:absolute;left:10px;top:6px}
.video-track{position:absolute;left:34px;top:10px;width:290px;height:3px;background:#555}

/* more line */
.more{position:absolute;height:34px;display:flex;align-items:center}
.more-line{height:2px;background:var(--ink);flex:1}
.more-btn{width:34px;height:34px;border:2px solid var(--ink);border-radius:50%;display:flex;align-items:center;justify-content:center;margin-left:4px;background:var(--white)}
.on-dark .more-line{background:var(--white)}
.on-dark .more-btn{border-color:var(--white);background:var(--navy)}

/* why */
.why{top:561px;height:539px;background:var(--navy);overflow:hidden;text-align:center;color:var(--white)}
.section-title{font-size:28px;font-weight:700}
.why .section-title{color:var(--blue);margin-top:100px}
.why .lead{margin-top:10px;font-size:11px;line-height:20px}
.phone{position:absolute;border:5px solid var(--white);border-bottom:none;border-radius:28px 28px 0 0;background:#15181e}
.phone-screen{position:absolute;left:10px;right:10px;top:40px;bottom:0}
.why .phone{left:517px;top:803px;width:187px;height:300px}
.why .phone-screen{background:linear-gradient(180deg,#2fb4ec,#1f9fd6);display:flex;align-items:center;justify-content:center}
.why .phone-screen .brand{color:var(--white);font-size:14px}
.why .phone-screen .brand-dot{background:var(--white);width:18px;height:18px}
.perk{position:absolute;width:116px;height:45px;border:1.5px dashed var(--blue);color:var(--blue);font-size:11px;font-weight:600;display:flex;align-items:center;justify-content:center;text-align:center;line-height:13px;padding:0 6px}
.perk.left{left:386px}
.perk.right{left:720px}

/* solutions */
.solutions{top:1100px;height:564px;background:linear-gradient(180deg,#3b4546 0%,#4a4a3e 55%,#6a563e 100%);color:var(--white);text-align:center}
.solutions-photo{position:absolute;inset:0;background:radial-gradient(ellipse at 58% 55%,var(--kraft) 0%,rgba(138,114,86,.4) 45%,transparent 75%)}
.solutions .section-title{position:relative;margin-top:135px}
.solutions .lead{position:relative;margin-top:8px;line-height:20px;font-size:11px}
.speech{position:absolute;left:521px;top:303px;width:372px;height:145px;background:var(--white);border-radius:6px;color:var(--ink);text-align:left;padding:16px 30px}
.speech::before{content:"";position:absolute;left:-14px;top:30px;border:14px solid transparent;border-right-color:var(--white);border-left:none}
.speech p{font-size:10.5px;line-height:20px}

/* europe */
.europe{top:1664px;height:382px;background:var(--navy);color:var(--white);overflow:hidden}
.europe .section-title{text-align:center;margin-top:46px}
.europe .phone{left:368px;top:116px;width:191px;height:270px}
.map-screen{background:linear-gradient(160deg,#e6e8ea,#cfd3d6)}
.copy{position:absolute;width:330px}
.copy p{margin-bottom:17px}

/* free */
.free{top:2046px;height:405px;background:var(--paper)}
.free .section-title{text-align:center;margin-top:66px}
.free-badge{left:295px;top:161px;width:207px;height:102px;background:linear-gradient(180deg,#3a3a3a,#111);border-radius:8px}

/* contact */
.contact{top:2451px;height:413px}
.work-map{left:0;top:0;width:620px;height:413px;background:linear-gradient(135deg,#d7dadd,#eceeef 60%,#dfe2e4)}
.contact-panel{left:620px;top:0;width:580px;height:413px;background:var(--navy);color:var(--white)}
.contact-panel .section-title{position:absolute;left:41px;top:52px}

/* footer */
.site-footer{top:2864px;height:183px;background:var(--paper);text-align:center}
.site-footer .brand{position:absolute;left:520px;top:34px}
.copyright{position:absolute;left:0;width:100%;top:90px;font-size:10px}
.copyright span{color:var(--blue)}
.social{position:absolute;top:130px;left:572px;display:flex;gap:12px}
.social i{display:block;width:18px;height:18px;border-radius:50%;background:var(--blue)}
</style>
</head>
<body>

<header class="hero">
  <svg class="hero-shape" width="1200" height="561" aria-hidden="true"><polygon points="600,0 1200,0 1200,561 262,561" fill="var(--sky)"/></svg>
  <nav class="site-nav">
    <div class="brand"><span class="brand-dot"></span>Movara Offers</div>
    <span class="nav-login">LOGIN</span>
    <span class="nav-register">REGISTER</span>
    <svg class="nav-icons" width="44" height="22" viewBox="0 0 44 22" aria-hidden="true">
      <circle cx="7" cy="8" r="5.5" fill="none" stroke="var(--ink)" stroke-width="2"/>
      <line x1="11" y1="12" x2="16" y2="17" stroke="var(--ink)" stroke-width="2.5"/>
      <rect x="26" y="3" width="17" height="3" fill="var(--ink)"/>
      <rect x="26" y="9.5" width="17" height="3" fill="var(--ink)"/>
      <rect x="26" y="16" width="17" height="3" fill="var(--ink)"/>
    </svg>
  </nav>
  <h1 class="abs hero-title">Looking for a transport company?<br>Looking for a loading?</h1>
  <div class="abs hero-copy">
    <p>We bring you together and find the best and most efficient way for your shipments.</p>
    <p>Movara offers is <strong>FREE</strong></p>
    <p>You are a few steps away from the easiest way to organize your transport.</p>
  </div>
  <div class="more" style="left:258px;top:423px;width:276px"><span class="more-line"></span><span class="more-btn"><svg width="12" height="12" viewBox="0 0 12 12"><path d="M3 1l6 5-6 5" fill="none" stroke="var(--ink)" stroke-width="2.5"/></svg></span></div>
  <div class="abs video" role="img" aria-label="Explanation video still showing a boy looking upward">
    <div class="video-bar">
      <svg class="video-play" width="10" height="10"><path d="M0 0l10 5-10 5z" fill="#fff"/></svg>
      <span class="video-track"></span>
    </div>
  </div>
</header>

<section class="why">
  <h2 class="section-title">Why should I use Movara offers?</h2>
  <p class="lead">People are definitely a company's greatest asset. It doesn't make any difference whether the product is cars or cosmetics.<br>A company is only as good as the people it keeps.</p>
  <div class="phone"><div class="phone-screen"><div class="brand"><span class="brand-dot"></span>Movara Offers</div></div></div>
  <div class="perk left" style="top:257px">Simple</div>
  <div class="perk left" style="top:324px">Actuel</div>
  <div class="perk left" style="top:395px">Great offer</div>
  <div class="perk left" style="top:464px">1 Invoice</div>
  <div class="perk right" style="top:297px">Quickly</div>
  <div class="perk right" style="top:364px;font-size:9px">Compare (who is the best provider, at what price)</div>
  <div class="perk right" style="top:436px">Independent</div>
</section>

<section class="solutions">
  <div class="solutions-photo" role="img" aria-label="Photo of a thoughtful man in a blue shirt sitting among stacked cardboard parcels"></div>
  <h2 class="section-title">Transport Solutions</h2>
  <p class="lead">People are definitely a company's greatest asset.<br>It doesn't make any difference</p>
  <div class="speech">
    <p>It is a long established fact that a reader will be distracted by the readable content of a page when looking at its layout. The point of using Lorem Ipsum is that it has a more-or-less normal distribution of letters, as opposed to using 'Content here, content here'.</p>
    <div class="more" style="left:30px;top:98px;width:298px"><span class="more-line"></span><span class="more-btn"><svg width="12" height="12" viewBox="0 0 12 12"><path d="M3 1l6 5-6 5" fill="none" stroke="var(--ink)" stroke-width="2.5"/></svg></span></div>
  </div>
</section>

<section class="europe">
  <h2 class="section-title">Destanition Europe</h2>
  <div class="phone"><div class="phone-screen map-screen" role="img" aria-label="Map of Europe centred on Poland with a location pin"></div></div>
  <div class="copy" style="left:614px;top:152px">
    <p>The standard chunk of Lorem Ipsum used since the 1500s is reproduced below for those interested. Sections 1.10.32 and 1.10.33 from "de Finibus Bonorum et Malorum" by Cicero are also reproduced in their exact original form, accompanied by English versions from the 1914 translation by H. Rackham.</p>
    <p>The standard chunk of Lorem Ipsum used since the 1500s is reproduced below for those interested. Sections.</p>
  </div>
</section>

<section class="free">
  <h2 class="section-title">Free</h2>
  <div class="abs free-badge" role="img" aria-label="Black ribbon badge reading Free"></div>
  <div class="copy" style="left:614px;top:137px">
    <p>The standard chunk of Lorem Ipsum used since the 1500s is reproduced below for those interested. Sections 1.10.32 and 1.10.33 from "de Finibus Bonorum et Malorum" by Cicero are also reproduced in their exact original form, accompanied by English versions from the 1914 translation by H. Rackham.</p>
    <p>The standard chunk of Lorem Ipsum used since the 1500s is reproduced below for those interested. Sections.</p>
  </div>
  <div class="more" style="left:614px;top:298px;width:268px"><span class="more-line"></span><span class="more-btn"><svg width="12" height="12" viewBox="0 0 12 12"><path d="M3 1l6 5-6 5" fill="none" stroke="var(--ink)" stroke-width="2.5"/></svg></span></div>
</section>

<section class="contact">
  <div class="abs work-map" role="img" aria-label="Map of Europe, Africa and Asia with blue markers showing the work area"></div>
  <div class="abs contact-panel on-dark">
    <h2 class="section-title">Contact</h2>
    <div class="copy" style="left:41px;top:136px;width:300px">
      <p>The standard chunk of Lorem Ipsum used since the 1500s is reproduced below for those interested. Sections 1.10.32 and 1.10.33 from "de Finibus Bonorum et Malorum".</p>
      <p style="margin-top:28px">The standard chunk of Lorem Ipsum used since the 1500s is reproduced below for those interested. Sections 1.10.32 and 1.10.33 from "de Finibus Bonorum et Malorum".</p>
    </div>
    <div class="more" style="left:41px;top:300px;width:276px"><span class="more-line"></span><span class="more-btn"><svg width="12" height="12" viewBox="0 0 12 12"><path d="M3 1l6 5-6 5" fill="none" stroke="var(--white)" stroke-width="2.5"/></svg></span></div>
  </div>
</section>

<footer class="site-footer">
  <div class="brand"><span class="brand-dot"></span>Movara Offers</div>
  <p class="copyright">© 2017 - <span>Movara Offers</span> All Right Reserved</p>
  <div class="social"><i></i><i></i><i></i></div>
</footer>

</body>
</html>
```